High Quality Business card for Property Management Agency - Super Classy and professional design

High Quality Business card design.

We need a business card designed for our Property Management Agency.
We are located on Sydney's Northern Beaches and manage beautiful properties along the beach and harbor.
We need a design that oozes modern, classy and professional.
I would like it to be double sided with contact details and logo on the front and just the logo on the back.

I need a print ready PDF version of the file as well as an editable photoshop (PSD) version of the file.

Logo and information details attached.

Target Market(s)

Property owners/investors, Male and Female Aged 28-65

Industry/Entity Type

Real Estate

Contact Information for Business Card

Tom Carrick
Tel: 0467 239 018
Email: tom@harvestlaneestates.com.au
Website: www.harvestlaneestates.com.au
Address: Level 2, 17 Wattlecourt Rd, Dunmarra NSW 2187

Font styles to use
Sans Serif

Requirements
Must have
• - Logo front and back
• - Business card details listed above and attached
• - Colour
Nice to have
• Sleek and professional

```html
<!DOCTYPE html>
<html lang="en">
<head>
<meta charset="utf-8">
<title>Harvest Lane Estates – Business Card</title>
<link rel="stylesheet" href="https://fonts.googleapis.com/css2?family=Source+Sans+3:wght@400;700&display=swap">
<style>
  :root {
    --backdrop: #5b5452;
    --card-dark: #3e3e40;
    --card-light: #ffffff;
    --teal: #2a9ca0;
    --ink: #141414;
    --text-light: #f2f2f2;
  }
  html, body {
    margin: 0;
    width: 1200px;
    height: 1200px;
    overflow: hidden;
    background: var(--backdrop);
    font-family: "Source Sans 3", sans-serif;
  }
  .card {
    position: absolute;
    left: 298px;
    width: 606px;
    height: 344px;
    box-shadow: 0 4px 14px rgba(0,0,0,0.35);
    overflow: hidden;
  }
  .card--front { top: 222px; background: var(--card-light); }
  .card--back { top: 636px; background: var(--card-dark); }
  .front-shape { position: absolute; inset: 0; width: 100%; height: 100%; }

  .brand {
    position: absolute;
    display: flex;
    align-items: center;
    gap: 10px;
    white-space: nowrap;
  }
  .brand__mark { width: 14px; height: 14px; background: var(--teal); flex: none; }
  .brand__mark--round { border-radius: 50%; }
  .brand__name {
    font-weight: 700;
    letter-spacing: 0.5px;
    line-height: 1;
  }
  .card--front .brand { right: 38px; top: 78px; }
  .card--front .brand__name { font-size: 30px; color: var(--ink); }
  .card--back .brand { left: 50%; top: 50%; transform: translate(-50%, -50%); }
  .card--back .brand__name { font-size: 36px; color: var(--text-light); }

  .contact { position: absolute; left: 28px; top: 186px; color: var(--text-light); }
  .contact__name {
    margin: 0 0 13px;
    font-size: 23px;
    font-weight: 700;
    color: var(--teal);
    letter-spacing: 0.3px;
  }
  .contact__list { list-style: none; margin: 0; padding: 0; }
  .contact__item {
    display: flex;
    align-items: center;
    height: 20px;
    font-size: 15px;
  }
  .contact__icon { width: 16px; height: 14px; margin-right: 12px; flex: none; }
  .contact__address { margin: 9px 0 0; font-size: 15px; }
</style>
</head>
<body>

<section class="card card--front" aria-label="Business card front">
  <svg class="front-shape" viewBox="0 0 757 430" preserveAspectRatio="none" aria-hidden="true">
    <polygon points="0,208 313,208 358,295 757,212 757,430 0,430" fill="var(--card-dark)"/>
    <polygon points="313,208 358,275 757,210 757,213 358,295" fill="var(--teal)"/>
  </svg>

  <div class="brand">
    <span class="brand__mark"></span>
    <span class="brand__name">HARVEST LANE ESTATES</span>
  </div>

  <div class="contact">
    <p class="contact__name">Tom Carrick</p>
    <ul class="contact__list">
      <li class="contact__item">
        <svg class="contact__icon" viewBox="0 0 16 14" aria-hidden="true">
          <path d="M1 5 Q8 0 15 5 L13 6 L11 4 L5 4 L3 6 Z" fill="var(--teal)"/>
          <rect x="3" y="7" width="10" height="6" rx="1" fill="var(--teal)"/>
          <circle cx="8" cy="10" r="1.6" fill="var(--card-dark)"/>
        </svg>
        0467 239 018
      </li>
      <li class="contact__item">
        <svg class="contact__icon" viewBox="0 0 16 14" aria-hidden="true">
          <rect x="1" y="2" width="14" height="10" fill="var(--teal)"/>
          <path d="M1 2 L8 8 L15 2 M1 12 L6 7 M15 12 L10 7" stroke="var(--card-dark)" stroke-width="1.2" fill="none"/>
        </svg>
        tom@harvestlaneestates.com.au
      </li>
      <li class="contact__item">
        <svg class="contact__icon" viewBox="0 0 16 16" aria-hidden="true">
          <g fill="none" stroke="var(--teal)" stroke-width="1.2">
            <circle cx="8" cy="8" r="6.5"/>
            <ellipse cx="8" cy="8" rx="3" ry="6.5"/>
            <path d="M1.5 8 H14.5 M2.5 4.5 H13.5 M2.5 11.5 H13.5"/>
          </g>
        </svg>
        www.harvestlaneestates.com.au
      </li>
    </ul>
    <p class="contact__address">Level 2, 17 Wattlecourt Rd, Dunmarra NSW 2187</p>
  </div>
</section>

<section class="card card--back" aria-label="Business card back">
  <div class="brand">
    <span class="brand__mark brand__mark--round"></span>
    <span class="brand__name">HARVEST LANE ESTATES</span>
  </div>
</section>

</body>
</html>
```